Self-Serve Brazilian Buffet and BBQ sold by the pound needs a business card

For CEO -Lucia Fernanda Matos Hale
Owner/President - Marcos Tiago Matos

Target Market(s)

Customers and

Industry/Entity Type

Business

Contact Information for Business Card

Lucia Fernanda Pinto Matos Hale
CEO of Vento Lume Grill
Brazilian BBQ Buffet sold by the pound

Requirements
Must have
• 5186 West Linden Blvd.
• Ste. K
• Santa Ana, CA 92704
• Phone : 555810-2947
• ventolumegrill@postrova.com

```html
<!DOCTYPE html>
<html lang="en">
<head>
<meta charset="utf-8">
<title>Vento Lume Grill — Business Card</title>
<link href="https://fonts.googleapis.com/css2?family=Marcellus&family=Open+Sans:wght@400;700&display=swap" rel="stylesheet">
<style>
  :root {
    --page-bg: #efece6;
    --green-dark: #6a9b3f;
    --green-light: #8dc63f;
    --cream-top: #f6ead0;
    --cream-bottom: #ecd9b0;
    --white: #ffffff;
    --name-green: #5f9a38;
    --title-brown: #6b4f2a;
    --brand-teal: #1f4b5c;
  }
  * { margin: 0; padding: 0; box-sizing: border-box; }
  html, body {
    width: 1200px;
    height: 1000px;
    overflow: hidden;
    background: var(--page-bg);
  }
  .card {
    position: absolute;
    left: 100px;
    top: 222px;
    width: 1000px;
    height: 556px;
    background: var(--white);
    box-shadow: 0 6px 18px rgba(0,0,0,0.18);
    overflow: hidden;
  }
  .card__top-stripe {
    height: 18px;
    background: var(--green-dark);
  }
  .card__brand-panel {
    height: 275px;
    background: linear-gradient(180deg, var(--cream-top), var(--cream-bottom));
    display: flex;
    align-items: center;
    justify-content: center;
    gap: 22px;
  }
  .brand-dot {
    width: 34px;
    height: 34px;
    border-radius: 50%;
    background: var(--green-dark);
  }
  .brand-name {
    font-family: "Marcellus", serif;
    font-size: 58px;
    color: var(--brand-teal);
    letter-spacing: 1px;
  }
  .card__accent-band {
    height: 27px;
    background: var(--green-light);
  }
  .card__identity {
    height: 107px;
    display: flex;
    flex-direction: column;
    align-items: center;
    justify-content: center;
  }
  .identity__name {
    font-family: "Marcellus", serif;
    font-size: 40px;
    color: var(--name-green);
    line-height: 1.1;
  }
  .identity__title {
    font-family: "Open Sans", sans-serif;
    font-weight: 700;
    font-size: 22px;
    color: var(--title-brown);
    margin-top: 4px;
  }
  .card__contact {
    height: 129px;
    background: var(--green-dark);
    display: flex;
    flex-direction: column;
    align-items: center;
    justify-content: center;
    font-family: "Open Sans", sans-serif;
    font-size: 23px;
    color: var(--white);
    line-height: 1.5;
    letter-spacing: 0.5px;
  }
</style>
</head>
<body>
  <main class="card">
    <div class="card__top-stripe"></div>
    <header class="card__brand-panel" role="img" aria-label="Vento Lume Grill name on a light cream wood-grain panel">
      <span class="brand-dot"></span>
      <span class="brand-name">Vento Lume Grill</span>
    </header>
    <div class="card__accent-band"></div>
    <section class="card__identity">
      <h1 class="identity__name">Lucia Fernanda Matos Hale</h1>
      <p class="identity__title">CEO</p>
    </section>
    <footer class="card__contact">
      <p>5186 West Linden Blvd., Ste. K, Santa Ana, CA 92704</p>
      <p>P : 555810-2947,&nbsp; E : ventolumegrill@postrova.com</p>
    </footer>
  </main>
</body>
</html>
```